Web Design Project for a new download application :-)

We need a website design and a logo design for a new website and desktop application.
The Website will be www.Fetchora.com
The installed application will be: Fetchora

Fetchora is a desktop application that searches and finds all kind of Media files (Movies, Games, Songs, software, etc..)
Fetchora will also manage the download process for the selected files.
Fetchora automates the whole search and download process.

User Flow:
users will initially visit the website.
user will download the application from the website
user will install the application on his computer.
user will run and use the application.

What makes our software special:
-Great search engine for searching media files.
-Very high speed downloads. maximum speeds.
-Allow used to Search by: file type, size, date, format
-Pause and resume downloads
-Get any file you want instantly.
-Unlimited Downloads.

We will need:
Logo
WebSite Design
Icons for the desktop application.

we need only PSDs - no codded pages are needed !

Design to the following screen Size & resolution: 1024 x 768

Target Market(s)

movies and music lovers.
users who download movies, games, softwares, music etc...

Industry/Entity Type

Software

Requirements
Must have
• must have download button

Files

```html
<!DOCTYPE html>
<html lang="en">
<head>
<meta charset="utf-8">
<title>Fetchora – Find and download any media</title>
<link rel="stylesheet" href="https://fonts.googleapis.com/css2?family=Arimo:wght@400;700&display=swap">
<style>
  :root {
    --blue: #2a6db5;
    --navy: #1c3f73;
    --hero-dark: #0d3a78;
    --hero-light: #3b7fd0;
    --text: #1a1a1a;
    --nav-grey: #555a60;
    --rule: #d4d4d4;
    --card: #ffffff;
    --page-top: #ffffff;
    --page-bottom: #a8a8a8;
    --tab-grey: #ececec;
    --link-blue: #245ea8;
  }
  * { box-sizing: border-box; margin: 0; padding: 0; }
  html, body { width: 1200px; height: 929px; overflow: hidden; }
  body {
    position: relative;
    font-family: "Arimo", Arial, sans-serif;
    color: var(--text);
    background: linear-gradient(to bottom, var(--page-top) 0, #f4f4f4 120px, #dcdcdc 600px, var(--page-bottom) 929px);
  }
  .brand {
    position: absolute; left: 48px; top: 34px;
    display: flex; align-items: center; gap: 10px;
    font-size: 56px; font-weight: 700; color: var(--blue); letter-spacing: -1px;
  }
  .brand-dot { width: 22px; height: 22px; border-radius: 50%; background: var(--blue); }
  .main-nav {
    position: absolute; right: 54px; top: 53px;
    display: flex; align-items: center; font-size: 17px; font-weight: 700; color: var(--nav-grey);
  }
  .main-nav a { color: inherit; text-decoration: none; }
  .main-nav .sep { margin: 0 12px; }
  .main-nav .current {
    display: inline-block; width: 83px; height: 29px; line-height: 29px; text-align: center;
    color: #fff; border-radius: 15px; margin-right: 14px;
    background: linear-gradient(#4f95e0, #1d5eb0); box-shadow: 0 0 0 1px #164a8c;
  }
  .card {
    position: absolute; left: 35px; top: 116px; width: 1123px; height: 718px;
    background: var(--card); border-radius: 6px; box-shadow: 0 2px 8px rgba(0,0,0,.12);
  }
  .hero {
    position: absolute; left: 9px; top: 0; width: 1107px; height: 394px;
    border-radius: 6px 6px 0 0; overflow: hidden;
    background: radial-gradient(circle at 40% 35%, var(--hero-light), #1c5aa8 45%, var(--hero-dark) 100%);
  }
  .hero-title { position: absolute; left: 35px; top: 40px; font-size: 46px; font-weight: 700; line-height: 48px; color: #fff; letter-spacing: -.5px; }
  .hero-title .accent { color: #9cc6f2; }
  .hero-text { position: absolute; left: 35px; top: 160px; width: 490px; font-size: 19px; line-height: 23px; color: #fff; }
  .btn {
    position: absolute; top: 300px; height: 39px; display: flex; align-items: center;
    font-size: 16px; font-weight: 700; color: #fff; text-transform: uppercase; text-shadow: 0 1px 1px rgba(0,0,0,.4);
  }
  .btn svg { position: absolute; left: 0; top: 0; }
  .btn span { position: relative; }
  .btn-download { left: 39px; width: 212px; }
  .btn-download span { padding-left: 50px; }
  .btn-more { left: 263px; width: 140px; }
  .btn-more span { padding-left: 18px; }
  .hero-media {
    position: absolute; right: 0; top: 9px; width: 567px; height: 385px;
    background: linear-gradient(110deg, #1a2a44 0, #3a5d8f 35%, #8a6a7a 70%, #c88aa8 100%);
  }
  .section-head { position: absolute; left: 35px; top: 417px; display: flex; align-items: center; gap: 12px; font-size: 21px; font-weight: 700; color: var(--navy); }
  .section-rule { position: absolute; left: 35px; top: 459px; width: 1052px; height: 1px; background: var(--rule); }
  .feature { position: absolute; top: 484px; width: 350px; }
  .feature-photo {
    position: absolute; left: 0; top: 0; width: 90px; height: 90px; border-radius: 50%;
    border: 4px solid #fff; box-shadow: 0 1px 5px rgba(0,0,0,.35);
  }
  .feature-body { position: absolute; left: 108px; top: 4px; width: 235px; font-size: 17px; line-height: 22px; }
  .feature-body h3 { font-size: 17px; color: var(--navy); }
  .feature-1 { left: 37px; } .feature-1 .feature-photo { background: linear-gradient(135deg, #6a4a3a, #c78a9a); }
  .feature-2 { left: 403px; } .feature-2 .feature-photo { background: linear-gradient(135deg, #3a3a3a, #4cae3a 60%, #555); }
  .feature-3 { left: 757px; } .feature-3 .feature-photo { background: linear-gradient(135deg, #cfd6de, #4a78b0); }
  .testimonial {
    position: absolute; left: 14px; top: 614px; width: 1091px; height: 68px;
    border: 1px solid #e2e2e2; border-radius: 3px; background: #fff;
  }
  .testimonial-tab { position: absolute; left: 0; top: 0; }
  .testimonial-title { position: absolute; left: 87px; top: 21px; font-size: 21px; color: var(--navy); }
  .testimonial-photo { position: absolute; left: 251px; top: 0; width: 78px; height: 67px; background: linear-gradient(#7a5a48, #2a2a2a); }
  .testimonial-quote { position: absolute; left: 343px; top: 16px; width: 720px; font-size: 14px; line-height: 20px; }
  .testimonial-quote strong { color: var(--link-blue); }
  .site-footer { position: absolute; left: 36px; top: 849px; font-size: 14px; line-height: 20px; color: #fff; }
  .site-footer a { color: #fff; text-decoration: none; }
  .newsletter { position: absolute; left: 702px; top: 853px; display: flex; align-items: center; }
  .newsletter label { font-size: 16px; font-weight: 700; color: #fff; margin: 0 10px 0 8px; }
  .newsletter .field {
    width: 196px; height: 29px; border: 1px solid #bbb; border-radius: 4px 0 0 4px; background: #fff;
    font: 14px "Arimo", Arial, sans-serif; color: #888; padding: 0 10px; line-height: 27px;
  }
  .newsletter .go { width: 30px; height: 29px; background: var(--link-blue); border-radius: 0 4px 4px 0; display: flex; align-items: center; justify-content: center; }
  .social { position: absolute; top: 850px; width: 36px; height: 36px; border-radius: 4px; }
  .social-a { left: 1076px; background: #3b5a9a; }
  .social-b { left: 1120px; background: #4fb8e6; }
</style>
</head>
<body>
  <div class="brand"><span class="brand-dot"></span>Fetchora</div>

  <nav class="main-nav">
    <a class="current" href="#">Home</a>
    <a href="#">About</a><span class="sep">|</span>
    <a href="#">Download</a><span class="sep">|</span>
    <a href="#">Blog</a><span class="sep">|</span>
    <a href="#">Contact</a>
  </nav>

  <main class="card">
    <section class="hero">
      <h1 class="hero-title">your website<br><span class="accent">caption goes</span> here</h1>
      <p class="hero-text">Lorem ipsum dolor sit amet, consectetur adipiscing elit. Morbi vestibulum augue turpis. Suspendisse porttitor dui nec risus malesuada eget porttitor enim elementum. Quisque nec tincidunt massa.</p>

      <a class="btn btn-download" href="#">
        <svg width="212" height="39" viewBox="0 0 212 39">
          <defs><linearGradient id="dl" x1="0" y1="0" x2="0" y2="1"><stop offset="0" stop-color="#3f82d4"/><stop offset="1" stop-color="#123f7e"/></linearGradient></defs>
          <path d="M2 2 H192 L209 19.5 L192 37 H2 Z" fill="url(#dl)" stroke="#fff" stroke-width="2.5"/>
          <path d="M14 -6 H32 V12 H40 L23 28 L6 12 H14 Z" fill="#6aa8e8" stroke="#fff" stroke-width="1.5"/>
        </svg>
        <span>Download Now</span>
      </a>
      <a class="btn btn-more" href="#">
        <svg width="140" height="39" viewBox="0 0 140 39">
          <defs><linearGradient id="rm" x1="0" y1="0" x2="0" y2="1"><stop offset="0" stop-color="#a8a8a8"/><stop offset="1" stop-color="#5a5a5a"/></linearGradient></defs>
          <path d="M2 2 H120 L137 19.5 L120 37 H2 Z" fill="url(#rm)" stroke="#fff" stroke-width="2.5"/>
        </svg>
        <span>Read More</span>
      </a>

      <div class="hero-media" role="img" aria-label="Photo of a smiling couple with a laptop beside a screen showing the Fetchora search window"></div>
    </section>

    <h2 class="section-head">
      <svg width="30" height="30" viewBox="0 0 30 30"><circle cx="15" cy="15" r="13.5" fill="#f2f2f2" stroke="#9a9a9a" stroke-width="1.5"/><path d="M8 12 H15 V7 L23 15 L15 23 V18 H8 Z" fill="#333"/></svg>
      Features &amp; Benefits
    </h2>
    <div class="section-rule"></div>

    <article class="feature feature-1">
      <div class="feature-photo" role="img" aria-label="Photo of two friends looking at a laptop"></div>
      <div class="feature-body"><h3>Pharetra faucibus luctus.</h3><p>Nulla facilisi. Donec eget mau vitae orci dignissim accumsan. Donec vulputate lorem vitae.</p></div>
    </article>
    <article class="feature feature-2">
      <div class="feature-photo" role="img" aria-label="Photo of a keyboard with a green download key"></div>
      <div class="feature-body"><h3>Pharetra faucibus luctus.</h3><p>Nulla facilisi. Donec eget mau vitae orci dignissim accumsan. Donec vulputate lorem vitae.</p></div>
    </article>
    <article class="feature feature-3">
      <div class="feature-photo" role="img" aria-label="Photo of a man relaxing with a laptop"></div>
      <div class="feature-body"><h3>Pharetra faucibus luctus.</h3><p>Nulla facilisi. Donec eget mau vitae orci dignissim accumsan. Donec vulputate lorem vitae.</p></div>
    </article>

    <aside class="testimonial">
      <svg class="testimonial-tab" width="240" height="66" viewBox="0 0 240 66">
        <path d="M0 0 H222 L240 33 L222 66 H0 Z" fill="var(--tab-grey)"/>
        <path d="M22 24 h24 a3 3 0 0 1 3 3 v14 a3 3 0 0 1 -3 3 h-14 l-8 6 v-6 h-2 a3 3 0 0 1 -3 -3 v-14 a3 3 0 0 1 3 -3z" fill="#8a8a8a"/>
        <path d="M36 17 h24 a3 3 0 0 1 3 3 v14 a3 3 0 0 1 -3 3 h-1 v6 l-7 -6 h-5 v-12 a5 5 0 0 0 -5 -5 h-9 v-0 a3 3 0 0 1 3 -3z" fill="#b0b0b0"/>
      </svg>
      <div class="testimonial-title">Happy Users</div>
      <div class="testimonial-photo" role="img" aria-label="Portrait photo of a satisfied user"></div>
      <p class="testimonial-quote">“Lorem ipsum dolor sit amet, consectetur adipiscing elit. Sed vel dui purus. Ut tincidunt convallis gravida. lorem, massa enim iaculis lectus, quis cursus dui dui a sapien. Sed pulvinar tempus enim.” <strong>Marcus, Perth</strong></p>
    </aside>
  </main>

  <footer class="site-footer">
    <p>Copyright © 2011 Fetchora. All rights Reserved.</p>
    <p><a href="#">Terms</a> &nbsp;|&nbsp; <a href="#">About Us</a> &nbsp;|&nbsp; <a href="#">Contact Us</a></p>
  </footer>

  <form class="newsletter">
    <svg width="18" height="16" viewBox="0 0 18 16"><path d="M1 6 L9 1 L17 6 V15 H1 Z" fill="#f4f4f4" stroke="#888"/><path d="M1 6 L9 11 L17 6" fill="none" stroke="#888"/></svg>
    <label>Enewsletter</label>
    <div class="field">enter your email address</div>
    <div class="go"><svg width="14" height="12" viewBox="0 0 14 12"><path d="M1 1 L6 6 L1 11 M7 1 L12 6 L7 11" fill="none" stroke="#fff" stroke-width="2"/></svg></div>
  </form>

  <div class="social social-a" role="img" aria-label="Social network link"></div>
  <div class="social social-b" role="img" aria-label="Social network link"></div>
</body>
</html>
```